Card design for orthopaedic surgeons working as The Brindlewood Orthopaedic Centre

Business cards, letterhead

Colors

Designer to choose colors to be used in the design.

Requirements
Must have
• Late addition.
• Cards letterhead must have logos of
• Corvane Federated Institute of Surgeons
• Meridale Orthopaedic Society
Nice to have
• Back of card to have space for appointment time to be added by hand and some blank space for writing incidental other notes.

```html
<!DOCTYPE html>
<html lang="en">
<head>
<meta charset="utf-8">
<title>The Brindlewood Orthopaedic Centre – Business Card</title>
<link rel="stylesheet" href="https://fonts.googleapis.com/css2?family=Mulish:wght@400;600;700&display=swap">
<style>
  :root {
    --navy: #0c2f4a;
    --sky: #4f97cf;
    --white: #ffffff;
    --paper: #f6f7f8;
    --ink: #0d2a44;
    --backdrop: #d9dcdf;
    --font: "Mulish", sans-serif;
  }
  html, body { margin: 0; padding: 0; overflow: hidden; }
  body {
    width: 1200px; height: 1021px;
    background: var(--backdrop);
    font-family: var(--font);
    position: relative;
  }
  .card {
    position: absolute;
    left: 250px;
    width: 700px; height: 400px;
    box-shadow: 0 6px 18px rgba(0,0,0,.18);
    overflow: hidden;
  }
  .card-back { top: 70px; background: var(--navy); }
  .card-front { top: 551px; background: var(--paper); }

  .wordmark {
    font-weight: 600;
    font-size: 27px;
    letter-spacing: -0.2px;
    white-space: nowrap;
    margin: 0;
  }
  .card-back .wordmark {
    position: absolute; top: 160px; left: 0; right: 0;
    text-align: center; color: var(--white);
  }
  .card-back .web {
    position: absolute; top: 300px; left: 0; right: 0; margin: 0;
    text-align: center; color: var(--white);
    font-size: 15px; letter-spacing: 1px;
  }

  .card-front .wordmark {
    position: absolute; top: 62px; left: 70px; color: var(--ink);
  }
  .card-front .swoosh { position: absolute; inset: 0; }
  .person { position: absolute; top: 148px; left: 50px; }
  .person-name {
    margin: 0; color: var(--sky); font-weight: 700; font-size: 22px;
  }
  .person-title {
    margin: 0; color: var(--ink); font-size: 16px;
  }
  .contact {
    position: absolute; right: 46px; top: 262px;
    text-align: right; color: var(--white);
    font-size: 18px; line-height: 23px;
  }
  .contact p { margin: 0; }
  .contact .address { margin-bottom: 8px; }
  .contact .line { display: flex; justify-content: flex-end; align-items: center; gap: 8px; }
  .contact .icon { width: 15px; height: 15px; flex: none; }
</style>
</head>
<body>

  <section class="card card-back" aria-label="Card back">
    <p class="wordmark">The Brindlewood Orthopaedic Centre</p>
    <p class="web">www.brindlewoodortho.com</p>
  </section>

  <section class="card card-front" aria-label="Card front">
    <svg class="swoosh" viewBox="0 0 700 400" width="700" height="400" aria-hidden="true">
      <path d="M0,250 Q330,150 700,238 L700,246 Q340,170 0,268 Z" fill="var(--sky)"/>
      <path d="M0,276 Q350,184 700,250 L700,400 L0,400 Z" fill="var(--navy)"/>
    </svg>

    <p class="wordmark">The Brindlewood Orthopaedic Centre</p>

    <div class="person">
      <p class="person-name">Daniel Ashcroft</p>
      <p class="person-title">Managing Director</p>
    </div>

    <div class="contact">
      <div class="address">
        <p>48 Harlow Crescent</p>
        <p>Fenwick Bay, 40217</p>
      </div>
      <p class="line">(555) 318-2047
        <svg class="icon" viewBox="0 0 16 16" aria-hidden="true"><path d="M3 1 L6 1 L7 5 L5 6.5 Q6.5 9.5 9.5 11 L11 9 L15 10 L15 13 Q15 15 13 15 Q1 14 1 3 Q1 1 3 1Z" fill="var(--sky)"/></svg>
      </p>
      <p class="line">daniel@brindlewoodortho.com
        <svg class="icon" viewBox="0 0 16 16" aria-hidden="true"><rect x="1" y="3" width="14" height="10" fill="none" stroke="var(--sky)" stroke-width="1.6"/><path d="M1 3 L8 9 L15 3" fill="none" stroke="var(--sky)" stroke-width="1.6"/></svg>
      </p>
      <p class="line">www.brindlewoodortho.com
        <svg class="icon" viewBox="0 0 16 16" aria-hidden="true"><circle cx="8" cy="8" r="6.5" fill="none" stroke="var(--sky)" stroke-width="1.4"/><ellipse cx="8" cy="8" rx="3" ry="6.5" fill="none" stroke="var(--sky)" stroke-width="1.2"/><path d="M1.5 8 H14.5 M2.5 4.8 H13.5 M2.5 11.2 H13.5" stroke="var(--sky)" stroke-width="1.1"/></svg>
      </p>
    </div>
  </section>

</body>
</html>
```